General Store Business Card Design

This is a general store with a post office, that sells groceries, papers, and has a café. It is in rural NSW. I would like to see very cheerful designs that have a cupcake and a cup of coffee as the main logo. This must have colours that will look good on a black background for future shirts for the business. For example, maybe a cupcake with pink frosting and a coffee cup that is a bright colour too. Would like the actual logo to be Wattle Bend General Store & Café wrapped around the logo picture. Would like for the background of the business card to also be colourful, ie: sprinkles, confetti, etc., with some sort of actual colour as a background as well.

Industry/Entity Type

Store

Contact Information for Business Card

Wattle Bend General Store & Café
48 Quelton Rd.
Wattle Bend, NSW, 2597
Phone: 02 5918 2640
Fax: 02 5918 ????
Website: www.??placeholder-tbd.example

Logo Text

Wattle Bend General Store & Cafe

```html
<!DOCTYPE html>
<html lang="en">
<head>
<meta charset="utf-8">
<title>Wattle Bend General Store &amp; Café – Business Card</title>
<link rel="stylesheet" href="https://fonts.googleapis.com/css2?family=Alegreya+SC:wght@400;700&display=swap">
<style>
  :root {
    --page-bg: #e6e6e6;
    --card-white: #ffffff;
    --pink-deep: #ee8a9c;
    --pink-light: #fde8ec;
    --ring-pink: #e96b87;
    --brown: #9a5a3a;
  }
  html, body {
    margin: 0;
    padding: 0;
    width: 1200px;
    height: 1000px;
    overflow: hidden;
    background: var(--page-bg);
    font-family: "Alegreya SC", Georgia, serif;
  }
  .card {
    position: absolute;
    left: 147px;
    top: 239px;
    width: 906px;
    height: 521px;
    background: var(--card-white);
    color: var(--brown);
  }
  .card__banner {
    position: absolute;
    left: 0;
    top: 0;
    width: 906px;
    height: 304px;
    background: radial-gradient(ellipse 60% 80% at 48% 55%, var(--pink-light) 0%, #f7c4ce 55%, var(--pink-deep) 100%);
  }
  .brand-mark {
    position: absolute;
    left: 333px;
    top: 69px;
    width: 200px;
    height: 200px;
  }
  .brand-mark__name {
    position: absolute;
    inset: 0;
    display: flex;
    flex-direction: column;
    align-items: center;
    justify-content: center;
    text-align: center;
    font-size: 19px;
    font-weight: 700;
    line-height: 1.2;
    color: var(--brown);
  }
  .business-name {
    position: absolute;
    left: 0;
    width: 906px;
    top: 310px;
    margin: 0;
    text-align: center;
    font-size: 29px;
    font-weight: 700;
    letter-spacing: 0.5px;
  }
  .website {
    position: absolute;
    left: 0;
    width: 906px;
    top: 352px;
    text-align: center;
    font-size: 17px;
    letter-spacing: 1px;
  }
  .address {
    position: absolute;
    left: 60px;
    top: 386px;
    margin: 0;
    font-style: normal;
    font-size: 21px;
    line-height: 28px;
  }
  .contact {
    position: absolute;
    right: 59px;
    top: 415px;
    text-align: right;
    font-size: 21px;
    line-height: 28px;
  }
</style>
</head>
<body>
  <div class="card">
    <div class="card__banner" role="img" aria-label="Pink background scattered with colourful sprinkles, confetti and curled ribbons"></div>

    <div class="brand-mark">
      <svg width="200" height="200" viewBox="0 0 200 200" aria-hidden="true">
        <circle cx="100" cy="100" r="96" fill="#fff6f8" stroke="var(--ring-pink)" stroke-width="5"/>
      </svg>
      <div class="brand-mark__name">Wattle Bend<br>General Store<br>&amp; Café</div>
    </div>

    <h1 class="business-name">Wattle Bend General Store &amp; Café</h1>
    <div class="website">WWW.??PLACEHOLDER-TBD.EXAMPLE</div>

    <address class="address">
      48 Quelton Rd,<br>
      Wattle Bend,<br>
      NSW, 2597
    </address>

    <div class="contact">
      Phone: 02 5918 2640<br>
      Fax: 02 5918 xxxx
    </div>
  </div>
</body>
</html>
```